Real estate company needs a letterhead design

A young real estate company needs a letterhead / stationery design, it should include the company's logo. It should look exactly the same as on the business cards. (With the phrase "a brand of KEV Wohnbau & Grundstücksentwicklung GmbH")

In addition, it should also include the 4 round seals.

color code blue # 00456b gray # 333333

Word and PDF are welcome.

KEV Wohnbau & Grundstücksentwicklung GmbH
Managing director: Mag. Lukas Fellnhuber
Matthias-Ortner-Strasse 3c / 41
6384 Bergfeldach

Tel .: +436648172093
Email: office@wohnglanz-beispiel.at
Web: www.wohnglanz-beispiel.at

Sparkasse Almtal, Bergländer Sparkasse from 1882, Genossenschaftskasse
Anton-Weissauer-Strasse 7, 6384 Bergfeldach
IBAN: AT31 4817 2964 0058 2316
BIC: GLMTAT44XXX
Account holder: KEV Wohnbau & Grundstücksentwicklung GmbH

FN: XXXXXXX
UID: XXXXXXX

```html
<!DOCTYPE html>
<html lang="de">
<head>
<meta charset="utf-8">
<title>Wohnglanz Letterhead</title>
<link href="https://fonts.googleapis.com/css2?family=Source+Sans+3:wght@400;600;700&display=swap" rel="stylesheet">
<style>
  :root {
    --brand-blue: #00456b;
    --brand-gray: #333333;
    --header-gray: #4a4a4a;
    --text-gray: #3c3c3c;
    --seal-red: #e0322b;
    --page: #ffffff;
    --backdrop: #000000;
  }
  * { margin: 0; padding: 0; box-sizing: border-box; }
  html, body { width: 960px; height: 1200px; overflow: hidden; background: var(--backdrop); }
  body { position: relative; font-family: "Source Sans 3", "Myriad Pro", Arial, sans-serif; color: var(--text-gray); }
  .sheet { position: absolute; left: 52px; top: 46px; width: 856px; height: 1108px; background: var(--page); }
  .abs { position: absolute; }

  .brand { left: 95px; top: 112px; }
  .brand-name { font-size: 41px; font-weight: 700; color: var(--brand-blue); letter-spacing: 0.5px; line-height: 1; display: flex; align-items: center; gap: 8px; }
  .brand-mark { width: 14px; height: 14px; background: var(--brand-blue); display: inline-block; }
  .brand-tagline { margin-top: 8px; font-size: 9.6px; font-weight: 700; color: var(--brand-gray); letter-spacing: -0.1px; }

  .header-band { left: 444px; top: 82px; width: 464px; height: 123px; background: var(--header-gray); }
  .name-tab { left: 422px; top: 100px; width: 218px; height: 42px; background: var(--brand-blue); color: #fff; padding: 5px 0 0 30px; font-size: 13.6px; line-height: 17px; }
  .name-tab strong { font-weight: 700; display: block; }
  .tab-fold { left: 422px; top: 142px; }
  .address { left: 470px; top: 145px; color: #fff; font-size: 13.2px; line-height: 17px; }
  .contacts { left: 706px; top: 111px; color: #fff; font-size: 13.2px; }
  .contact { display: flex; align-items: center; gap: 6px; height: 23px; white-space: nowrap; }
  .contact svg { width: 17px; height: 17px; flex: none; }

  .salutation { left: 124px; top: 325px; font-size: 15.5px; }
  .letter-body { left: 124px; top: 395px; width: 712px; font-size: 16.4px; line-height: 20.2px; text-align: justify; }
  .letter-body p + p { margin-top: 20.5px; }
  .letter-body p:first-child { text-indent: 50px; }

  .footer-rule { left: 96px; top: 983px; }
  .bank { left: 96px; top: 1005px; font-size: 13px; line-height: 17px; }
  .foot-col { top: 1062px; font-size: 13px; line-height: 17px; }
  .foot-col strong { font-weight: 700; }
  .col-iban { left: 96px; }
  .col-holder { left: 290px; }
  .col-reg { left: 500px; top: 1079px; }
  .divider { top: 1057px; width: 2px; height: 74px; background: var(--brand-gray); border-radius: 1px; }
  .seals { left: 612px; top: 1065px; display: flex; gap: 6px; }
  .seal { width: 64px; height: 64px; border-radius: 50%; border: 2px solid var(--seal-red); display: flex; align-items: center; justify-content: center; }
  .seal span { width: 40px; height: 40px; border-radius: 50%; background: var(--seal-red); }
</style>
</head>
<body>
  <div class="sheet"></div>

  <div class="abs brand">
    <div class="brand-name"><span class="brand-mark"></span>WOHNGLANZ</div>
    <div class="brand-tagline">eine Marke der KEV Wohnbau &amp; Grundstücksentwicklung GmbH</div>
  </div>

  <div class="abs header-band"></div>
  <svg class="abs tab-fold" width="24" height="9" viewBox="0 0 24 9"><polygon points="0,0 24,0 24,9" fill="#002b44"/></svg>
  <div class="abs name-tab"><strong>Mag. Lukas Fellnhuber</strong>Managing director:</div>
  <div class="abs address">Matthias-Ortner-Strasse 3c / 41<br>6384 Bergfeldach</div>

  <div class="abs contacts">
    <div class="contact">
      <svg viewBox="0 0 17 17"><rect width="17" height="17" rx="2" fill="#fff"/><path d="M5 3.5l2 0 1 3-1.3 1a7 7 0 0 0 2.8 2.8l1-1.3 3 1 0 2a1.5 1.5 0 0 1-1.6 1.4A9 9 0 0 1 3.6 5.1 1.5 1.5 0 0 1 5 3.5z" fill="var(--brand-blue)"/></svg>
      +436648172093
    </div>
    <div class="contact">
      <svg viewBox="0 0 17 17"><rect width="17" height="17" rx="2" fill="#fff"/><rect x="3" y="5" width="11" height="7.5" fill="none" stroke="var(--brand-blue)" stroke-width="1.3"/><path d="M3 5l5.5 4.5L14 5" fill="none" stroke="var(--brand-blue)" stroke-width="1.3"/></svg>
      office@wohnglanz-beispiel.at
    </div>
    <div class="contact">
      <svg viewBox="0 0 17 17"><rect width="17" height="17" rx="2" fill="#fff"/><g fill="none" stroke="var(--brand-blue)" stroke-width="1.1"><circle cx="8.5" cy="8.5" r="5.5"/><ellipse cx="8.5" cy="8.5" rx="2.4" ry="5.5"/><path d="M3 8.5h11M4 5.8h9M4 11.2h9"/></g></svg>
      www.wohnglanz-beispiel.at
    </div>
  </div>

  <div class="abs salutation">Dear Dr</div>

  <div class="abs letter-body">
    <p>Lorem ipsum dolor sit amet, consectetur adipiscing elit. Integer eu odio mattis, pulvinar turpis quis, faucibus nisl. Proin feugiat, erat vitae cursus pharetra, enim est semper ligula, in malesuada orci nisl et diam. Etiam elementum metus ac fringilla vulputate. Etiam mattis ligula sed ante mollis bibendum. Orci varius natoque penatibus et magnis dis parturient montes, nascetur ridiculus mus.</p>
    <p>Ut nibh augue, blandit ac orci ac, rutrum congue enim. Suspendisse gravida vulputate felis, quis interdum orci tincidunt quis. Praesent imperdiet maximus neque. Mauris ut dui enim. Nullam at efficitur elit. Donec ante ipsum, fermentum at lectus vel, blandit vulputate ante. Proin luctus suscipit diam id vestibulum. Morbi malesuada id mauris eget ullamcorper.</p>
    <p>Donec varius orci purus, vitae aliquam libero volutpat id. Integer sed imperdiet libero. Aliquam accumsan, risus sit amet ornare consectetur, turpis felis dictum justo, non rhoncus mauris dui sed velit. Pellentesque habitant morbi tristique senectus et netus et malesuada fames ac turpis egestas. Pellentesque tincidunt vitae ligula nec imperdiet. Donec sed congue enim. Nullam elementum faucibus nulla nec vestibulum. Sed at tempor ligula. In quis vulputate nunc. Integer at gravida lacus, ac tristique risus. Sed at vulputate nulla.</p>
    <p>Praesent blandit nunc eu efficitur commodo. In tempor nisi ex, vel venenatis ante vestibulum a. Duis vestibulum nibh a erat sagittis, nec euismod lorem varius. Nam ultricies turpis sed justo sollicitudin volutpat. Morbi sed mollis eros. Sed quis tortor id enim vehicula porttitor. Curabitur non aliquam ex. Phasellus dignissim fermentum elit, at finibus ligula mattis eget.</p>
  </div>

  <svg class="abs footer-rule" width="768" height="6" viewBox="0 0 768 6"><polygon points="0,3 384,0.6 768,3 384,5.4" fill="var(--brand-gray)"/></svg>

  <div class="abs bank">Sparkasse Almtal, Bergländer Sparkasse from 1882, Genossenschaftskasse<br>Anton-Weissauer-Strasse 7, 6384 Bergfeldach</div>

  <div class="abs foot-col col-iban"><strong>IBAN:</strong><br>AT31 4817 2964 0058 2316<br>BIC: GLMTAT44XXX</div>
  <div class="abs divider" style="left:272px"></div>
  <div class="abs foot-col col-holder"><strong>Account holder:</strong><br>KEV Wohnbau &amp;<br>Grundstücksentwicklung GmbH</div>
  <div class="abs divider" style="left:478px"></div>
  <div class="abs foot-col col-reg"><strong>FN:</strong> XXXXXXX<br><strong>UID:</strong> XXXXXXX</div>
  <div class="abs divider" style="left:600px"></div>

  <div class="abs seals">
    <div class="seal" role="img" aria-label="Quality seal"><span></span></div>
    <div class="seal" role="img" aria-label="Quality seal"><span></span></div>
    <div class="seal" role="img" aria-label="Quality seal"><span></span></div>
    <div class="seal" role="img" aria-label="Quality seal"><span></span></div>
  </div>
</body>
</html>
```